Pedicure Menu with 8 Scent Options

This design will be for a single page menu (front/back) that will display multiple different scent variations of a product. The purpose of this menu is to display to clients and show them the available options and benefits of each option.
The menu will be double sided.
The front page will include a header including brand logo and product name, and a total of 8 different scents including imagery and descriptive text.
The design should include the text provided for each scent. The design should have a layout that is structured/organized, easy to read, and has bright imagery that represents each scent.
An example is a modular layout using boxes that highlight a different scent within each box. Lavender scent should include aesthetic images of lavender flower and/or the color purple.
The back page will include brand logo, overall product description, and additional brief text that explains each step of the product.
The final size of the design should be 8.5"x11", produced in InDesign format, with all layers editable for future changes.
NOTE: Please carefully review the attached design brief that includes additional information, and all necessary text to include in the design.
Target Market(s)
Beauty/Spa Clients
Industry/Entity Type
Beauty
Requirements
Must have
- Bright and Vivid Imagery/Illustrations
Nice to have
- Background design that utilizes, lines, shapes, or other elements.

```html
<!DOCTYPE html>
<html lang="en">
<head>
<meta charset="utf-8">
<title>Petalwick Deluxe Pedicure Menu</title>
<link href="https://fonts.googleapis.com/css2?family=Poppins:wght@300;400;600;700&display=swap" rel="stylesheet">
<style>
:root{
  --stage:#d9d9da;
  --paper-a:#f1f1f2;
  --paper-b:#dfe0e2;
  --ink:#231f20;
  --band:#252223;
  --white:#ffffff;
  --lavender:#8b67bd;
  --mandarin:#f26b21;
  --jasmine:#f4dc7c;
  --cucumber:#7cc143;
  --mint:#1db5ad;
  --rose:#e2232b;
  --honey:#f6b42a;
  --greentea:#4c9e40;
}
*{box-sizing:border-box;margin:0;padding:0}
html,body{width:751px;height:1200px;overflow:hidden}
body{background:var(--stage);font-family:'Poppins',sans-serif;color:var(--ink);position:relative}
.page{
  position:absolute;left:147px;width:456px;height:588px;
  background:radial-gradient(circle at 30% 20%,var(--paper-a),var(--paper-b) 70%,var(--paper-a));
  box-shadow:2px 3px 6px rgba(0,0,0,.25);
}
.page--front{top:6px}
.page--back{top:606px}
.brand{height:60px;display:flex;align-items:center;justify-content:center}
.brand__name{font-weight:400;font-size:30px;color:var(--ink);line-height:1}
.band{background:var(--band);color:var(--white);text-align:center;font-weight:300}
.band--title{font-size:16px;height:30px;line-height:30px}
.subtitle{text-align:center;font-size:15px;font-weight:300;height:30px;line-height:30px}
.scents{display:grid;grid-template-columns:1fr 1fr;gap:13px 16px;padding:4px 13px 0 13px}
.scent{position:relative;height:98px;display:flex;background:var(--white);
  border-right:4px solid var(--c);border-bottom:4px solid var(--c);border-radius:5px;
  box-shadow:1px 2px 3px rgba(0,0,0,.2)}
.scent__img{width:72px;flex:none;border-radius:5px 0 0 5px}
.scent__body{flex:1;padding-top:8px}
.scent__name{background:var(--c);color:var(--white);font-weight:700;font-size:11px;padding:2px 8px;border-radius:4px 4px 0 0}
.scent__name--dark{color:var(--ink)}
.scent__text{font-size:5.3px;line-height:1.38;padding:5px 8px 0 8px;text-align:justify}
.lavender{--c:var(--lavender)}
.mandarin{--c:var(--mandarin)}
.jasmine{--c:var(--jasmine)}
.cucumber{--c:var(--cucumber)}
.mint{--c:var(--mint)}
.rose{--c:var(--rose)}
.honey{--c:var(--honey)}
.greentea{--c:var(--greentea)}
.band--intro{font-size:10.5px;line-height:1.35;padding:7px 12px;height:64px;display:flex;align-items:center;justify-content:center}
.steps{display:grid;grid-template-columns:1fr 1fr;gap:20px 24px;padding:18px 22px 0 22px}
.step{background:var(--white);border:2px solid var(--band);border-radius:8px;overflow:hidden;height:204px;display:flex;flex-direction:column;box-shadow:3px 4px 0 var(--band)}
.step__img{flex:1}
.step__name{background:var(--band);color:var(--white);text-align:center;font-weight:700;font-size:15px;height:22px;line-height:22px}
.step__text{text-align:center;font-size:10px;line-height:1.3;padding:4px 8px 6px;font-weight:400}
</style>
</head>
<body>

<section class="page page--front">
  <header class="brand"><span class="brand__name">Petalwick</span></header>
  <h1 class="band band--title">Deluxe Pedicure 4-Step</h1>
  <h2 class="subtitle">Pick Your Pedicure</h2>
  <div class="scents">
    <article class="scent lavender">
      <div class="scent__img" role="img" aria-label="Bundle of lavender flowers" style="background:linear-gradient(160deg,#fff,#d9cdf0 60%,#9a7fc9)"></div>
      <div class="scent__body"><h3 class="scent__name">Lavender</h3>
      <p class="scent__text">Melt away the stresses of the day with a delicate, sweet smell that is floral and woodsy at the same time. Lavender is a calming scent for relaxation that puts us in a better mood and helps create a sense of tranquility and peacefulness.</p></div>
    </article>
    <article class="scent mandarin">
      <div class="scent__img" role="img" aria-label="Peeled mandarin oranges" style="background:linear-gradient(160deg,#fff,#fbc27c 55%,#f08a1e)"></div>
      <div class="scent__body"><h3 class="scent__name">Mandarin</h3>
      <p class="scent__text">Uplift your senses with a fruity and sweet aroma that promotes clarity, radiance and a smooth, even skin tone. A citrus blend of essential oils works great to polish dull skin, reduce wrinkles, and correct spots.</p></div>
    </article>
    <article class="scent jasmine">
      <div class="scent__img" role="img" aria-label="White jasmine blossoms" style="background:linear-gradient(160deg,#fff,#f4f2e6 55%,#b7cf95)"></div>
      <div class="scent__body"><h3 class="scent__name scent__name--dark">Jasmine</h3>
      <p class="scent__text">Embrace the warmth of a rich and sensual floral scent that boosts your energy levels and helps make your day better and brighter. A symbol of purity, love, and beauty – Jasmine helps to reduce exhaustion, nervousness, and stress.</p></div>
    </article>
    <article class="scent cucumber">
      <div class="scent__img" role="img" aria-label="Sliced cucumber and cantaloupe melon" style="background:linear-gradient(160deg,#fff,#f7c58d 50%,#a9d68a)"></div>
      <div class="scent__body"><h3 class="scent__name">Cucumber-Melon</h3>
      <p class="scent__text">Jump into a refreshing blend of crisp cucumber, watery honeydew, and summer cantaloupe. Perfect for capturing the essence of a summer day. Bamboo and aloe extract help cool your skin after a day in the sun.</p></div>
    </article>
    <article class="scent mint">
      <div class="scent__img" role="img" aria-label="Fresh mint leaves" style="background:linear-gradient(160deg,#fff,#a8dc86 55%,#4fa83a)"></div>
      <div class="scent__body"><h3 class="scent__name">Mint</h3>
      <p class="scent__text">Rejuvenate your body with a cool mix of peppermint and spearmint that prevents skin damage, alleviates inflamed skin, and acts as a splash of tonic for the senses. Infused with eucalyptus to leave you clean, cool, and crisp.</p></div>
    </article>
    <article class="scent rose">
      <div class="scent__img" role="img" aria-label="Red roses" style="background:linear-gradient(160deg,#fff,#e95058 50%,#a5121a)"></div>
      <div class="scent__body"><h3 class="scent__name">Rose</h3>
      <p class="scent__text">Fall in love with a delicate floral twist of spicy and sweet that nourishes your skin and calms the mind. Essential oils help to reduce fine lines and protect the skin from UV damage.</p></div>
    </article>
    <article class="scent honey">
      <div class="scent__img" role="img" aria-label="Milk bottle and honey jar with honeycomb" style="background:linear-gradient(160deg,#fff,#fbe2a6 50%,#f0a51c)"></div>
      <div class="scent__body"><h3 class="scent__name scent__name--dark">Milk &amp; Honey</h3>
      <p class="scent__text">Discover one of nature's most luxurious skin cleansers and softeners. Creamy milk is full of rich essential vitamins that supply abundant moisture and improves skin elasticity. Sweet honey contains antioxidants and other nutrients that slow down skin aging.</p></div>
    </article>
    <article class="scent greentea">
      <div class="scent__img" role="img" aria-label="Green tea leaves and dried tea" style="background:linear-gradient(160deg,#fff,#9fd27a 50%,#3f8a2d)"></div>
      <div class="scent__body"><h3 class="scent__name">Green-Tea</h3>
      <p class="scent__text">Restore a sense of serenity with fragrant green tea extract that helps to relax the mind, reduces redness and swelling, and leaves the skin feeling hydrated, silky, and smooth. A natural detoxification that will supplies abundant moisture to the skin.</p></div>
    </article>
  </div>
</section>

<section class="page page--back">
  <header class="brand"><span class="brand__name">Petalwick</span></header>
  <p class="band band--intro">Petalwick Deluxe Pedicure 4-Step will transform your pedicure experience<br>and immerse your senses into a floral paradise designed to<br>rejuvenate your body. Sit back, relax, and enjoy</p>
  <div class="steps">
    <article class="step">
      <div class="step__img" role="img" aria-label="Foot dipping into a soaking bowl among greenery" style="background:linear-gradient(180deg,#6f9b4f,#b9cfa0 55%,#ece9e4)"></div>
      <h3 class="step__name">Salt Soak</h3>
      <p class="step__text">Detoxifies and deodorizes<br>your feet</p>
    </article>
    <article class="step">
      <div class="step__img" role="img" aria-label="Hands applying sugar scrub to skin" style="background:linear-gradient(180deg,#e8c8b6,#f3e1d6 55%,#d9b29c)"></div>
      <h3 class="step__name">Sugar Scrub</h3>
      <p class="step__text">Detoxifies and deodorizes<br>your feet</p>
    </article>
    <article class="step">
      <div class="step__img" role="img" aria-label="Gloved hands applying a foot masque" style="background:linear-gradient(180deg,#e9e6e4,#efb4c8 50%,#7a1f24)"></div>
      <h3 class="step__name">Foot Masque</h3>
      <p class="step__text">Detoxifies and deodorizes<br>your feet</p>
    </article>
    <article class="step">
      <div class="step__img" role="img" aria-label="Relaxing spa massage scene" style="background:linear-gradient(180deg,#cfe3e0,#e6c3ae 55%,#f1ece8)"></div>
      <h3 class="step__name">Massage Lotion</h3>
      <p class="step__text">Detoxifies and deodorizes<br>your feet</p>
    </article>
  </div>
</section>

</body>
</html>
```